Harbor Fieldworks (Business Card Design)

Need business cards designed. Something modern, chic, and sleek. Mabye the back of the card should be the navy blue that is in the logo and then just the logo on the back.

Target Market(s)

Those in the hotel, office, and renovation industry

Contact Information for Business Card

1. Logo 2. Dorian Velasko 3. CEO/Founder 4. Phone: (833) HarbFld / (833) 427-2353 5. Email: dorian@theharborfieldworks.com 6. Website: www.theharborfieldworks.com

Font styles to use
Other font styles liked:
• Look at the logo font and base the font for everything else off of that.

Colors
0054AA
0677BA
7BADD7
CADEEF
E8F1F8

Requirements
Must have
• Colors that are associated in the logo
Nice to have
• Sleek modern clean and chic design.

```html
<!DOCTYPE html>
<html lang="en">
<head>
<meta charset="utf-8">
<title>Harbor Fieldworks — Business Card</title>
<link href="https://fonts.googleapis.com/css2?family=Raleway:wght@400;500;700&display=swap" rel="stylesheet">
<style>
  :root {
    --navy: #0b1a45;
    --gold: #d6a94a;
    --white: #ffffff;
    --paper: #f7f7f7;
    --backdrop: #3a3a3a;
  }
  * { margin: 0; padding: 0; box-sizing: border-box; }
  html, body { width: 1200px; height: 1200px; overflow: hidden; }
  body {
    background: var(--backdrop);
    font-family: "Raleway", sans-serif;
    position: relative;
  }
  .card {
    position: absolute;
    left: 150px;
    width: 900px;
    height: 514px;
    border-radius: 40px;
    overflow: hidden;
    box-shadow: 0 10px 30px rgba(0,0,0,0.4);
  }
  .card-front { top: 60px; display: flex; }
  .card-back { top: 626px; background: var(--navy); display: flex; align-items: center; justify-content: center; }

  .contact-panel {
    width: 530px;
    height: 100%;
    background: var(--navy);
    padding: 0 0 0 92px;
    display: flex;
    flex-direction: column;
    justify-content: center;
  }
  .gold-rule { width: 13px; height: 100%; background: var(--gold); }
  .gap-rule { width: 9px; height: 100%; background: var(--white); }
  .brand-panel {
    flex: 1;
    background: linear-gradient(180deg, var(--white), var(--paper));
    display: flex;
    align-items: center;
    justify-content: center;
  }

  .person-name {
    color: var(--gold);
    font-weight: 700;
    font-size: 34px;
    letter-spacing: -0.5px;
    line-height: 1;
  }
  .person-role {
    color: var(--white);
    font-size: 22px;
    margin: 6px 0 20px 24px;
  }
  .contact-list { list-style: none; }
  .contact-list li {
    display: flex;
    align-items: center;
    gap: 12px;
    color: var(--white);
    font-size: 19px;
    line-height: 1.45;
    white-space: nowrap;
  }
  .contact-list .no-icon { padding-left: 34px; }
  .contact-list svg { width: 22px; height: 22px; flex: none; }

  .wordmark {
    display: flex;
    align-items: center;
    gap: 18px;
  }
  .wordmark-square { width: 22px; height: 22px; background: var(--gold); flex: none; }
  .wordmark-name {
    font-weight: 700;
    font-size: 30px;
    letter-spacing: 3px;
    line-height: 1.15;
    text-transform: uppercase;
    color: var(--navy);
  }
  .card-back .wordmark-name { color: var(--white); font-size: 46px; letter-spacing: 5px; }
  .card-back .wordmark-square { width: 32px; height: 32px; }
</style>
</head>
<body>
  <section class="card card-front">
    <div class="contact-panel">
      <div class="person-name">DORIAN VELASKO</div>
      <div class="person-role">CEO | FOUNDER</div>
      <ul class="contact-list">
        <li class="no-icon">(833) HarbFld | (833) 427-2353</li>
        <li>
          <svg viewBox="0 0 24 24" fill="var(--gold)"><path d="M6.6 10.8a15 15 0 0 0 6.6 6.6l2.2-2.2c.3-.3.7-.4 1-.2 1.1.4 2.3.6 3.6.6.6 0 1 .4 1 1V20c0 .6-.4 1-1 1A17 17 0 0 1 3 4c0-.6.4-1 1-1h3.5c.6 0 1 .4 1 1 0 1.3.2 2.5.6 3.6.1.3 0 .7-.2 1z"/></svg>
          dorian@theharborfieldworks.com
        </li>
        <li>
          <svg viewBox="0 0 24 24" fill="none" stroke="var(--gold)" stroke-width="2"><rect x="2" y="5" width="20" height="14"/><path d="M2 5l10 8 10-8"/></svg>
          www.theharborfieldworks.com
        </li>
      </ul>
    </div>
    <div class="gold-rule"></div>
    <div class="gap-rule"></div>
    <div class="brand-panel">
      <div class="wordmark">
        <span class="wordmark-square"></span>
        <span class="wordmark-name">Harbor<br>Fieldworks</span>
      </div>
    </div>
  </section>

  <section class="card card-back">
    <div class="wordmark">
      <span class="wordmark-square"></span>
      <span class="wordmark-name">Harbor<br>Fieldworks</span>
    </div>
  </section>
</body>
</html>
```